Harbor Lantern Wellness Foundation branding and promotion

I need a brochure (not the typical trifold (maybe 5X5 with 5 or 6 segments). It needs to deliver several strong points: who we are, why we exist, what we do, how we do it, and DONATE now.We are a fairly new Foundation in the Veteran space, a very crowded space. I need a design that will separate us and clearly state: who we are (our story), what we do, how we do it and why. Our website is www.hlwf-sample.us

Target Market(s)

Corporate America, Veterans, their family members, the members of the community where they live, work, play and pray

Font styles to use
Serif

Colors
ffc214
faa54b
f68d4d
e34197

Requirements
Must have
• "CURB APPEAL", it must grab the target market and COMPEL them to volunteer, donate, sponsor foundation activities.
• Pictures
• Graphics
• Review website for content, I will then expand, edit, etc.
Nice to have
• For colors, see the colors in the logo. Other complementary colors can be used

```html
<!DOCTYPE html>
<html lang="en">
<head>
<meta charset="utf-8">
<title>Harbor Lantern Wellness Foundation – Brochure</title>
<link href="https://fonts.googleapis.com/css2?family=Didact+Gothic&family=Mulish:wght@400;700;800&display=swap" rel="stylesheet">
<style>
  :root{
    --stage:#bccfd6;
    --paper:#ffffff;
    --ink:#262626;
    --magenta:#e0389a;
    --magenta-deep:#b8307f;
    --magenta-top:#d43a97;
    --amber:#fdb84f;
    --orange:#f9a41c;
    --grey:#6b7075;
  }
  *{margin:0;padding:0;box-sizing:border-box}
  html,body{width:1200px;height:344px;overflow:hidden;background:var(--stage)}
  .brochure{
    position:absolute;left:20px;top:56px;width:1160px;height:231px;
    display:flex;background:var(--paper);
    box-shadow:2px 3px 5px rgba(0,0,0,.35);
    font-family:"Didact Gothic",sans-serif;color:var(--ink);
  }
  .panel{position:relative;height:100%;overflow:hidden;flex:none}
  .vision{width:232px;background:var(--paper)}
  .about{width:232px;background:var(--magenta);color:#fff}
  .photo{width:259px;background:var(--paper)}
  .stats{width:205px;background:var(--paper)}
  .cover{width:232px;background:var(--paper)}

  .corner{position:absolute;left:0;top:0;width:30px;height:35px}
  .vision .corner{background:var(--amber)}
  .about .top-band{position:absolute;left:0;top:0;width:100%;height:35px;background:var(--magenta-top)}
  .about .corner{background:var(--magenta-deep)}

  .panel-title{
    position:absolute;left:31px;top:38px;
    font-family:"Mulish",sans-serif;font-weight:700;font-size:17px;
    font-variant:small-caps;letter-spacing:2px;line-height:1;
  }
  .vision .panel-title{color:var(--magenta)}
  .about .panel-title{color:#fff}
  .copy{
    position:absolute;left:32px;top:58px;width:172px;
    font-size:7px;line-height:9px;
  }
  .about .copy{left:31px;width:173px;text-align:justify}
  .copy p+p{margin-top:9px}
  .copy ul{list-style:none}
  .copy li::before{content:"•\00a0\00a0"}

  .photo-area{
    position:absolute;left:0;top:35px;width:100%;height:196px;
    background:
      radial-gradient(ellipse 60% 45% at 30% 20%,#86c24e 0%,rgba(134,194,78,0) 70%),
      linear-gradient(180deg,#5c9b35 0%,#497f2e 38%,#3a4a48 62%,#23282c 100%);
  }

  .stats-lead{
    position:absolute;left:17px;top:34px;width:161px;
    font-family:"Mulish",sans-serif;font-weight:800;font-size:6.6px;line-height:9px;text-align:justify;
  }
  .stat-list{position:absolute;left:17px;top:70px;width:162px;list-style:none}
  .stat-list li{
    position:relative;padding-left:11px;font-size:7px;line-height:7.8px;
    text-align:justify;margin-bottom:7.6px;
  }
  .stat-list li::before{
    content:"";position:absolute;left:0;top:1.5px;width:5px;height:5px;
    background:var(--magenta);box-shadow:-1px -1px 0 #f08ac6;
  }
  .stat-list b{font-family:"Mulish",sans-serif;font-weight:800}
  .site{
    position:absolute;left:0;top:219px;width:100%;text-align:center;
    font-size:5px;letter-spacing:1.8px;text-transform:uppercase;
  }
  .stats .site{color:var(--magenta)}
  .cover .site{color:#fff}

  .brand-dot{
    position:absolute;left:50%;top:24px;width:22px;height:22px;margin-left:-11px;
    border-radius:50%;background:var(--magenta);
  }
  .brand{
    position:absolute;left:0;top:50px;width:100%;text-align:center;
    font-family:"Didact Gothic",sans-serif;font-size:12.5px;line-height:13.5px;color:var(--grey);
  }
  .collage{
    position:absolute;left:0;top:86px;width:100%;height:111px;
    display:grid;grid-template-columns:70px 80px 82px;grid-template-rows:56px 55px;
  }
  .tile{display:block}
  .t1{background:linear-gradient(160deg,#f0b43a,#b87410)}
  .t2{background:linear-gradient(200deg,#f7c25a,#d08a14)}
  .t3{background:linear-gradient(140deg,#fbd27a,#e29d20)}
  .t4{background:linear-gradient(120deg,#c98414,#eaa82c)}
  .t5{background:linear-gradient(180deg,#f3b845,#c07c0e)}
  .t6{background:linear-gradient(150deg,#e9a628,#f6c766)}
  .cover-band{position:absolute;left:0;top:197px;width:100%;height:34px;background:var(--orange)}
</style>
</head>
<body>
<main class="brochure">

  <section class="panel vision">
    <div class="corner"></div>
    <h2 class="panel-title">Our Vission</h2>
    <div class="copy">
      <p>HLWF envisions a world in which ALL veterans and their families live healthy and well lives undiminished by their service related health concerns.<br>
      HLWF approaches its vision with passion and purpose to ensure we:</p>
      <ul>
        <li>Amplify the veteran community voice in the battle for health and wellness</li>
        <li>Advocate for equitable healthcare for veterans and their families</li>
        <li>Gather and disseminate knowledge regarding veterans’ health, healthcare and wellness to veterans, their families and the communities in which they live</li>
        <li>Develop and disseminate free education and training to healthcare professionals that address the health and wellness of veterans’ and their families</li>
      </ul>
    </div>
  </section>

  <section class="panel about">
    <div class="top-band"></div>
    <div class="corner"></div>
    <h2 class="panel-title">About</h2>
    <div class="copy">
      <p>Harbor Lantern Wellness Foundation (HLWF) is a non-profit 501c3 charitable entity established in 2013 by military veterans with expertise in healthcare, for the express purpose of addressing systemic inequities regarding access to and quality of care for veterans and their families.</p>
      <p>Having committed their lives to our country, Veterans leave military service with a host of potentially debilitating health conditions—not just PTSD and traumatic brain injury, but autoimmune disorders, hearing loss, lung disorders, chemical exposure related heart problems, musculoskeletal injuries, and a host of other potential problems many that remain unknown for years after discharge or retirement.</p>
    </div>
  </section>

  <section class="panel photo">
    <div class="photo-area" role="img" aria-label="Photo of three smiling veterans in uniform and caps standing together outdoors among green trees"></div>
  </section>

  <section class="panel stats">
    <p class="stats-lead">The numbers of veterans and their families in in need of help are substantial:</p>
    <ul class="stat-list">
      <li><b>19 million</b> discharged Americans warriors are either currently suffering multiple chronic conditions</li>
      <li>brought on by the conditions of their military service or are at risk.</li>
      <li><b>54 million</b> family members are also affected.</li>
      <li><b>75 million</b> total number of those needing some form of specialized care.</li>
      <li>These 75 million Americans represent about 25% of the entire U.S. population in need of some form of specialized or unique care.</li>
    </ul>
    <p class="site">www.hlwf-sample.us</p>
  </section>

  <section class="panel cover">
    <span class="brand-dot"></span>
    <div class="brand">Harbor Lantern<br>Wellness Foundation</div>
    <div class="collage" role="img" aria-label="Orange-toned collage of six photos showing veterans, families and healthcare professionals in care settings">
      <span class="tile t1"></span><span class="tile t2"></span><span class="tile t3"></span>
      <span class="tile t4"></span><span class="tile t5"></span><span class="tile t6"></span>
    </div>
    <div class="cover-band"></div>
    <p class="site">www.hlwf-sample.us</p>
  </section>

</main>
</body>
</html>
```